Velmaran Business Card

Business card for philanthropic organization

Industry/Entity Type

Business

Contact Information for Business Card

Need a very ELEGANT, sober, embossed, formal business card... it should transmit CREDIBILITY. Not looking for a "fun card". would like white, grays or black designs.

Font styles to use
Script

Requirements
Must have
• Embossed look

```html
<!DOCTYPE html>
<html lang="en">
<head>
<meta charset="utf-8">
<title>Velmaran Business Card</title>
<link rel="stylesheet" href="https://fonts.googleapis.com/css2?family=Lato:wght@300;400&family=Dancing+Script:wght@500&family=Patrick+Hand&display=swap">
<style>
  :root {
    --page: #e6e3de;
    --card-dark: #0c0c0c;
    --card-mid: #2b2b2b;
    --card-sheen: #3a3a3a;
    --ink: #f1f1f1;
    --ink-soft: #c9c9c9;
    --rule: #d8d8d8;
    --mark: #dedede;
  }
  * { margin: 0; padding: 0; box-sizing: border-box; }
  html, body { width: 1200px; height: 1023px; overflow: hidden; background: var(--page); }
  .canvas { position: relative; width: 1200px; height: 1023px; }
  .card {
    position: absolute; left: 75px; top: 211px; width: 1050px; height: 600px;
    border-radius: 6px; overflow: hidden;
    background:
      linear-gradient(115deg, transparent 30%, rgba(255,255,255,0.07) 42%, transparent 52%),
      radial-gradient(ellipse at 38% 60%, var(--card-sheen) 0%, var(--card-mid) 30%, var(--card-dark) 80%);
    box-shadow: 0 18px 40px rgba(0,0,0,0.35);
  }
  .card-header {
    position: absolute; left: 44px; top: 40px;
    font-family: "Lato", sans-serif; font-weight: 300; font-size: 31px; letter-spacing: 0.5px;
    color: var(--ink); text-shadow: 0 -1px 0 rgba(0,0,0,0.8), 0 1px 0 rgba(255,255,255,0.15);
  }
  .brand {
    position: absolute; left: 150px; top: 300px;
    display: flex; align-items: center; gap: 18px;
  }
  .brand-dot { width: 46px; height: 46px; border-radius: 50%; background: var(--mark); }
  .brand-name {
    font-family: "Dancing Script", cursive; font-weight: 500; font-size: 60px; color: var(--mark);
  }
  .divider {
    position: absolute; left: 560px; top: 215px; width: 2px; height: 230px;
    background: var(--rule);
  }
  .contact { position: absolute; left: 610px; top: 190px; color: var(--ink); }
  .contact-name {
    font-family: "Dancing Script", cursive; font-weight: 500; font-size: 66px; line-height: 1;
    text-shadow: 0 -1px 0 rgba(0,0,0,0.8), 0 1px 0 rgba(255,255,255,0.18);
  }
  .contact-role {
    font-family: "Dancing Script", cursive; font-size: 22px; color: var(--ink-soft);
    margin: 4px 0 14px 34px;
  }
  .contact-lines { list-style: none; font-family: "Patrick Hand", cursive; font-size: 29px; line-height: 40px; }
  .contact-lines li { display: flex; align-items: center; gap: 10px; }
  .contact-lines svg { width: 22px; height: 22px; flex: none; }
</style>
</head>
<body>
<div class="canvas">
  <section class="card">
    <p class="card-header">Tomás Elizondo&nbsp; Al Varesh Velmaran Potentate 2017</p>

    <div class="brand">
      <span class="brand-dot"></span>
      <span class="brand-name">Velmaran</span>
    </div>

    <div class="divider"></div>

    <div class="contact">
      <h1 class="contact-name">Daniel Morrow</h1>
      <p class="contact-role">Director</p>
      <ul class="contact-lines">
        <li>P.O. Box 0712-05518</li>
        <li>Coronado, Republic of Panama</li>
        <li>
          <svg viewBox="0 0 24 24" aria-hidden="true"><path d="M6 3l3 4-2 2c1 3 4 6 7 7l2-2 4 3-2 3C10 20 4 14 3 5z" fill="#f1f1f1"/></svg>
          +(507)-6120-4482
        </li>
        <li>
          <svg viewBox="0 0 24 24" aria-hidden="true"><rect x="3" y="6" width="18" height="12" fill="none" stroke="#f1f1f1" stroke-width="2"/><path d="M3 6l9 7 9-7" fill="none" stroke="#f1f1f1" stroke-width="2"/></svg>
          telizondo@velmaran.org
        </li>
      </ul>
    </div>
  </section>
</div>
</body>
</html>
```